Business Card Design Project

I need a business card design for an Organic drive thru coffee kiosk. We will serve organic coffee, teas & smoothies and will serve healthy breakfast food/snacks for people on the go.
I want the card to have 2-3 colors max (earthy colors like browns, greens and so on).
I have attached the logo I want used and would love to play off the theme of "balance."
Include:
Sun-Grove Coffee
address: 4170 Pelham Ct. Raleigh, NC 27593
phone: 919-307-4462
website: www.sun-grove-example.com (website is not up yet but still include it on card)
email: Dorothy@sun-grove-example.com
I want one of the following sayings somewhere on the card (the front or back is fine):
"Eat & Drink Well, on the run!"
"Break the fast with Sun-Grove"
Maybe on the back list what we offer:
-Organic coffee, espresso & tea
-Blendora smoothies & protein shakes
-Zesty Tonic (100% fresh local fruit and veggies)
-Healthy Bites

```html
<!DOCTYPE html>
<html lang="en">
<head>
<meta charset="utf-8">
<title>Sun-Grove Coffee – Business Card</title>
<link rel="stylesheet" href="https://fonts.googleapis.com/css2?family=Federo&family=Open+Sans:wght@400&display=swap">
<style>
  :root {
    --backdrop: #2b2b2b;
    --card-brown: #4b2c1c;
    --card-brown-deep: #3f2416;
    --band-tan: #c8975f;
    --name-panel: #7d6257;
    --name-ink: #3a2014;
    --accent-rust: #a9553a;
    --text-tan: #d9a86c;
    --text-cream: #e6c99d;
  }
  * { margin: 0; padding: 0; box-sizing: border-box; }
  html, body { width: 1200px; height: 876px; overflow: hidden; background: var(--backdrop); }
  .canvas { position: relative; width: 1200px; height: 876px; }

  .card {
    position: absolute;
    width: 620px;
    height: 354px;
    background: linear-gradient(90deg, var(--card-brown-deep), var(--card-brown) 40%, var(--card-brown-deep));
    overflow: hidden;
    font-family: "Open Sans", sans-serif;
    box-shadow: 0 6px 18px rgba(0,0,0,.45);
  }
  .card--front { left: 60px; top: 60px; }
  .card--back { left: 520px; top: 462px; }

  .band { position: absolute; left: 0; right: 0; bottom: 0; background: var(--band-tan); }
  .card--front .band { height: 20px; }
  .card--back .band {
    height: 42px;
    display: flex; align-items: center; justify-content: center;
    color: var(--card-brown-deep);
    font-size: 21px; letter-spacing: 7px;
  }

  .bean-scatter {
    position: absolute; left: 18px; top: 30px; width: 210px; height: 290px;
    background: radial-gradient(ellipse at 45% 55%, rgba(169,85,58,.55), rgba(169,85,58,.15) 70%, transparent 85%);
  }

  .mark-dot {
    position: absolute; border-radius: 50%; background: var(--accent-rust);
  }
  .card--front .mark-dot { left: 250px; top: 110px; width: 84px; height: 84px; }
  .card--back .mark-dot { left: 60px; top: 160px; width: 110px; height: 110px; }

  .name-panel {
    position: absolute;
    background: var(--name-panel);
    display: flex; flex-direction: column; align-items: center; justify-content: center;
  }
  .card--front .name-panel { left: 350px; top: 90px; width: 250px; height: 92px; }
  .card--back .name-panel { left: 330px; top: 128px; width: 260px; height: 92px; }

  .brand-name {
    font-family: "Federo", sans-serif;
    font-size: 44px; line-height: 1;
    color: var(--name-ink);
  }
  .brand-tagline {
    margin-top: 6px;
    font-size: 10px; letter-spacing: 3px; text-transform: uppercase;
    color: var(--accent-rust);
  }

  .slogan {
    position: absolute; left: 350px; top: 192px;
    font-size: 17px; color: var(--text-cream);
  }

  .offer-list {
    position: absolute; left: 26px; top: 16px;
    list-style: none;
    font-size: 14px; line-height: 18px; color: var(--text-cream);
  }

  .contact {
    position: absolute; left: 190px; top: 232px;
    display: grid; grid-template-columns: 82px auto; row-gap: 4px; column-gap: 18px;
    font-size: 16px;
  }
  .contact dt { color: var(--text-tan); }
  .contact dd { color: var(--text-cream); }
</style>
</head>
<body>
<main class="canvas">

  <section class="card card--front" aria-label="Card front">
    <div class="bean-scatter" role="img" aria-label="Scattered coffee bean pattern"></div>
    <span class="mark-dot" aria-hidden="true"></span>
    <div class="name-panel">
      <span class="brand-name">Sun-Grove</span>
      <span class="brand-tagline">Organic coffee + cafe</span>
    </div>
    <p class="slogan">Break the fast with Sun-Grove</p>
    <div class="band"></div>
  </section>

  <section class="card card--back" aria-label="Card back">
    <ul class="offer-list">
      <li>-Organic coffee, espresso &amp; tea</li>
      <li>-Blendora smoothies &amp; protein shakes</li>
      <li>-Zesty Tonic (100% fresh local fruit and veggies)</li>
      <li>-Healthy Bites</li>
    </ul>
    <span class="mark-dot" aria-hidden="true"></span>
    <div class="name-panel">
      <span class="brand-name">Sun-Grove</span>
      <span class="brand-tagline">Organic coffee + cafe</span>
    </div>
    <dl class="contact">
      <dt>Address:</dt><dd>4170 Pelham Ct. Raleigh, NC 27593</dd>
      <dt>Phone:</dt><dd>919-307-4462</dd>
      <dt>Email:</dt><dd>Dorothy@sun-grove-example.com</dd>
    </dl>
    <div class="band">www.sun-grove-example.com</div>
  </section>

</main>
</body>
</html>
```